Computer repair services flyer

This flyer / leaflet is required to promote my local computer and laptop repair business. It will primarily be used for pinning to notice boards when I get access to shared accommodation but I will also use it in the future for posting through letterboxes in affluent areas.

Company branding, logo, services, pricing, contact details etc. can be found on my website at : www.brightlanetech.co.uk

The services I would predominantly like to promote on this flyer are :

Speeding up slow / old computers
Virus removal
Lost data recovered
Broken laptop screen replacements
Dead laptops fixed
We buy and recycle broken laptops for cash

Other features to highlight :

Friendly and experienced
We are local (Near to Cardiff city center)
Quick repair turnaround - most repairs within 24hours
Affordable / No VAT
Free diagnostics
No Fix = No fee
Free collection and delivery
We Guarantee our work

Calls to action and attention grabbing if possible. Offer 10% off. Free cooling fan clean.

Size of flyer = A5 (210 x 148mm or 8.3 x 5.8in) portrait, single sided colour.

Target Market(s)

18 to 60 years

Industry/Entity Type

Accommodation

Requirements
Must have
• 02940 613857

```html
<!DOCTYPE html>
<html lang="en">
<head>
<meta charset="utf-8">
<title>Bright Lane Tech – Computer Repair Flyer</title>
<link rel="stylesheet" href="https://fonts.googleapis.com/css2?family=Nunito:wght@700;900&family=Roboto+Slab:wght@700;800&display=swap">
<style>
  :root {
    --paper: #f4f4f4;
    --panel: #5b5b5b;
    --panel-dark: #4a4a4a;
    --orange: #f7941d;
    --orange-deep: #e0661a;
    --white: #ffffff;
    --tick: #7cc242;
    --ink-grey: #6a6a6a;
    --gold: #e3b23c;
    --gold-deep: #b8801c;
    --badge-red: #c8282d;
  }
  html, body { margin: 0; padding: 0; overflow: hidden; }
  body { width: 847px; height: 1200px; background: var(--paper); font-family: "Nunito", Arial, sans-serif; }
  .flyer { position: relative; width: 847px; height: 1200px; overflow: hidden; background: var(--paper); }
  .backdrop { position: absolute; inset: 0; }
  .hero-art {
    position: absolute; left: 85px; top: 55px; width: 470px; height: 330px;
    border-radius: 24px;
    background: linear-gradient(160deg, #ffffff 0%, #d9dde2 60%, #b9bfc6 100%);
  }
  .photo-circle {
    position: absolute; border-radius: 50%;
    border: 6px solid var(--white);
    box-shadow: 0 4px 12px rgba(0,0,0,.35);
  }
  .photo-parts { left: 430px; top: 225px; width: 180px; height: 180px; background: radial-gradient(circle at 40% 40%, #8a8f96, #2f3135); }
  .photo-screen { left: 238px; top: 425px; width: 140px; height: 140px; background: radial-gradient(circle at 50% 45%, #5fa8e6, #1c4f8a 70%, #e9eef3 71%); }
  .brand {
    position: absolute; right: 24px; top: 28px;
    display: flex; align-items: center; gap: 12px;
    color: var(--panel-dark); font-weight: 900; font-size: 34px; letter-spacing: .5px;
  }
  .brand-dot { width: 22px; height: 22px; background: var(--orange); border-radius: 50%; }
  .services { position: absolute; left: 540px; top: 478px; width: 300px; margin: 0; padding: 0; list-style: none; }
  .service {
    position: relative; padding: 9px 42px 9px 0; text-align: center;
    color: var(--orange); font-family: "Roboto Slab", Georgia, serif; font-weight: 800; font-size: 20px; line-height: 1.15;
    border-bottom: 2px solid rgba(255,255,255,.55);
  }
  .service:last-child { border-bottom: none; }
  .service svg { position: absolute; right: 2px; bottom: 8px; width: 34px; height: 29px; }
  .fan-offer {
    position: absolute; left: 80px; top: 640px; width: 240px; text-align: center;
    color: var(--orange); font-family: "Roboto Slab", Georgia, serif; font-weight: 800; font-size: 32px; line-height: 1.1; margin: 0;
  }
  .discount-badge {
    position: absolute; left: 110px; top: 740px; width: 130px; height: 130px;
    border-radius: 50%; background: radial-gradient(circle at 40% 35%, #f7d774, var(--gold) 55%, var(--gold-deep));
    display: flex; align-items: center; justify-content: center;
    box-shadow: 0 4px 10px rgba(0,0,0,.35);
  }
  .discount-badge span {
    background: var(--badge-red); color: var(--white); font-weight: 900; font-size: 22px;
    padding: 3px 12px; border-radius: 4px;
  }
  .call-now { position: absolute; left: 60px; top: 920px; margin: 0; color: var(--orange); font-family: "Roboto Slab", Georgia, serif; font-weight: 800; font-size: 56px; line-height: 1; }
  .phone { position: absolute; left: 40px; top: 1010px; margin: 0; color: var(--white); font-weight: 900; font-size: 58px; line-height: 1; letter-spacing: 1px; }
  .footer {
    position: absolute; left: 0; top: 1100px; width: 847px; height: 100px; background: var(--panel-dark);
  }
  .footer p {
    position: absolute; left: 22px; top: 12px; width: 660px; margin: 0;
    color: var(--white); font-weight: 700; font-size: 16px; line-height: 1.45;
  }
  .map-area {
    position: absolute; right: 14px; top: 10px; width: 120px; height: 80px;
    background: linear-gradient(135deg, #e7ecdf, #cfd9c4 60%, #b9c9e0);
    border: 1px solid #c8c8c8;
  }
</style>
</head>
<body>
<div class="flyer">
  <svg class="backdrop" width="847" height="1200" viewBox="0 0 847 1200" aria-hidden="true">
    <path d="M0 300 C 220 250, 520 330, 847 250 L 847 1100 L 0 1100 Z" fill="var(--panel)"/>
    <path d="M0 280 C 220 230, 520 310, 847 230" fill="none" stroke="var(--orange)" stroke-width="14"/>
    <path d="M0 318 C 240 270, 520 350, 847 272" fill="none" stroke="var(--orange-deep)" stroke-width="6"/>
  </svg>

  <div class="hero-art" role="img" aria-label="Illustration of a white computer monitor with an orange first-aid cross on screen"></div>

  <div class="brand"><span class="brand-dot"></span>Bright Lane Tech</div>

  <div class="photo-circle photo-parts" role="img" aria-label="Photo of an opened laptop with repair parts"></div>
  <div class="photo-circle photo-screen" role="img" aria-label="Photo of a monitor showing gears"></div>

  <ul class="services">
    <li class="service">Speeding up slow / old computers<svg viewBox="0 0 40 34"><path d="M3 18 L14 29 L37 4" fill="none" stroke="var(--tick)" stroke-width="6" stroke-linecap="round" stroke-linejoin="round"/></svg></li>
    <li class="service">Virus removal<svg viewBox="0 0 40 34"><path d="M3 18 L14 29 L37 4" fill="none" stroke="var(--tick)" stroke-width="6" stroke-linecap="round" stroke-linejoin="round"/></svg></li>
    <li class="service">Lost data recovered<svg viewBox="0 0 40 34"><path d="M3 18 L14 29 L37 4" fill="none" stroke="var(--tick)" stroke-width="6" stroke-linecap="round" stroke-linejoin="round"/></svg></li>
    <li class="service">Broken laptop screen replacements<svg viewBox="0 0 40 34"><path d="M3 18 L14 29 L37 4" fill="none" stroke="var(--tick)" stroke-width="6" stroke-linecap="round" stroke-linejoin="round"/></svg></li>
    <li class="service">Dead laptops fixed<svg viewBox="0 0 40 34"><path d="M3 18 L14 29 L37 4" fill="none" stroke="var(--tick)" stroke-width="6" stroke-linecap="round" stroke-linejoin="round"/></svg></li>
    <li class="service">We buy and recycle broken laptops for cash<svg viewBox="0 0 40 34"><path d="M3 18 L14 29 L37 4" fill="none" stroke="var(--tick)" stroke-width="6" stroke-linecap="round" stroke-linejoin="round"/></svg></li>
  </ul>

  <p class="fan-offer">Free cooling fan clean!</p>

  <div class="discount-badge"><span>10% OFF</span></div>

  <p class="call-now">Call now!</p>
  <p class="phone">02940 613857</p>

  <div class="footer">
    <p>Friendly and experienced - Near to Cardiff city center - Quick repair turnaround most repairs within 24hours - Affordable / No VAT - Free diagnostics - No Fix = No fee - Free collection and delivery - We Guarantee our work</p>
    <div class="map-area" role="img" aria-label="Small street map of Cardiff city centre"></div>
  </div>
</div>
</body>
</html>
```